Clear Cash Blueprint: 8 Simple Steps To Put Your Family Budget On Track

Need a book cover for a book called "Clear Cash Blueprint: 8 Steps To Put Your Family Budget On Track"

The book is 5.5 by 8.5 and has no spine.

I am attaching the current cover but would like to see some other options that you all can come up with.

This book contains 8 specific action items for what people need to do.
Pay down debt. get estate documents in order. Be careful when buying a house, have enough life insurance to pay debt...etc.

Target Market(s)

Target market is parents around 35-55 years old who are concerned about their financial situation.

Industry/Entity Type

Financial Planning

Font styles to use
Serif

Colors

Designer to choose colors to be used in the design.

Requirements
Must have
• Definitely want my picture on the back.
Nice to have
• I'm pretty much open to ideas.

```html
<!DOCTYPE html>
<html lang="en">
<head>
<meta charset="utf-8">
<title>Clear Cash Blueprint – Book Cover</title>
<link href="https://fonts.googleapis.com/css2?family=Josefin+Sans:wght@300;400&family=EB+Garamond:ital,wght@1,400&display=swap" rel="stylesheet">
<style>
  :root {
    --cover-bg: #f79494;
    --cover-floor: #f9a3a1;
    --ink-dark: #363636;
    --ink-light: #ffffff;
    --pig-light: #f4a6c8;
    --pig-mid: #e27fb0;
    --pig-dark: #c95f95;
  }
  html, body {
    margin: 0;
    padding: 0;
    width: 777px;
    height: 1200px;
    overflow: hidden;
    background: var(--cover-bg);
  }
  .cover {
    position: relative;
    width: 777px;
    height: 1200px;
    overflow: hidden;
    background: radial-gradient(ellipse at 50% 70%, #f89c9b 0%, var(--cover-bg) 60%);
  }
  .title-art {
    position: absolute;
    left: 0;
    top: 0;
    width: 777px;
    height: 320px;
  }
  .title-line {
    font-family: "Josefin Sans", sans-serif;
  }
  .title-line--top { fill: var(--ink-light); font-weight: 300; }
  .title-line--main { fill: var(--ink-dark); font-weight: 300; }
  .rule {
    position: absolute;
    height: 3px;
    background: var(--ink-dark);
  }
  .rule--upper { left: 75px; width: 608px; top: 377px; }
  .rule--lower { left: 69px; width: 609px; top: 547px; }
  .subtitle {
    position: absolute;
    left: 40px;
    width: 697px;
    top: 404px;
    margin: 0;
    text-align: center;
    font-family: "EB Garamond", serif;
    font-style: italic;
    font-weight: 400;
    font-size: 39px;
    line-height: 54px;
    letter-spacing: 1px;
    color: var(--ink-dark);
  }
  .floor {
    position: absolute;
    left: 0;
    top: 985px;
    width: 777px;
    height: 215px;
    background: linear-gradient(to bottom, #fbb0ad 0%, var(--cover-floor) 25%, var(--cover-bg) 100%);
  }
  .hero-figure {
    position: absolute;
    left: 236px;
    top: 677px;
    width: 313px;
    height: 308px;
    border-radius: 46% 46% 30% 30%;
    background: radial-gradient(ellipse at 45% 35%, var(--pig-light) 0%, var(--pig-mid) 55%, var(--pig-dark) 100%);
  }
  .author-art {
    position: absolute;
    left: 0;
    top: 1060px;
    width: 777px;
    height: 80px;
  }
  .author-name {
    font-family: "Josefin Sans", sans-serif;
    font-weight: 300;
    fill: var(--ink-dark);
  }
</style>
</head>
<body>
  <main class="cover">
    <svg class="title-art" viewBox="0 0 777 320" aria-label="Clear Cash Blueprint">
      <text class="title-line title-line--top" x="62" y="156" font-size="112" textLength="663" lengthAdjust="spacingAndGlyphs">CLEAR CASH</text>
      <text class="title-line title-line--main" x="68" y="300" font-size="160" textLength="641" lengthAdjust="spacingAndGlyphs">BLUEPRINT</text>
    </svg>

    <div class="rule rule--upper"></div>
    <p class="subtitle">8 Steps To Put Your Family Budget<br>On Track</p>
    <div class="rule rule--lower"></div>

    <div class="floor"></div>
    <div class="hero-figure" role="img" aria-label="Glossy pink piggy bank standing on the floor"></div>

    <svg class="author-art" viewBox="0 0 777 80" aria-label="Dana Whitcombe">
      <text class="author-name" x="62" y="65" font-size="64" textLength="647" lengthAdjust="spacing">DANA WHITCOMBE</text>
    </svg>
  </main>
</body>
</html>
```